Swing Tag for a sustainable fashion label

Our capsule clothing collections are sustainable and ethically made in beautiful Newcastle, Australia. Our customer 's are stylish women 35-70, all shapes and sizes.<br/>14cm x 5cm<br/> <br/>Our logo on one side, with Made in Australia underneath it, as per our label.<br/> <br/>On the reverse I would like something like a checklist, so we can tick the appropriate circle to match the garment:<br/>I’d like the circle’s bigger and line up LHS.<br/>Same font as the logo.<br/>With the body shape section is it possible to have an image similar to the ones attached for inspiration.<br/>Black on white except for the shading of the body shape over the figure sketch.<br/> <br/>Colour <br/>o Cool<br/>o Neutral<br/>o Warm<br/> <br/>Body Shape<br/> <br/>o Rectangle<br/>o Triangle<br/>o Inverted Triangle<br/>o Diamond<br/>o Round<br/>o Diamond<br/>o Hourglass<br/> <br/>This piece looks great worn..<br/>…………………………………………..<br/>…………………………………………...<br/>………………………………………….<br/>………………………………………….<br/>………………………………………….<br/>www.lanternandmoss.com.au

Target Market(s)

35 -70 women

Industry/Entity Type

Fashion

Colors
f9d9e8

Requirements
Must have
• See attached for logo and inspiration
Nice to have
• as above

```html
<!DOCTYPE html>
<html lang="en">
<head>
<meta charset="utf-8">
<title>Lantern &amp; Moss – Swing Tag</title>
<link rel="stylesheet" href="https://fonts.googleapis.com/css2?family=Josefin+Slab:wght@400;700&family=Josefin+Sans:wght@700&family=Arvo:wght@700&display=swap">
<style>
  :root {
    --ink: #000000;
    --paper: #ffffff;
    --backdrop: #d9ceb2;
    --blush: #f2a7cb;
    --blush-soft: #f9d9e8;
  }
  * { margin: 0; padding: 0; box-sizing: border-box; }
  html, body { width: 800px; height: 1200px; overflow: hidden; }
  body { background: var(--backdrop); position: relative; color: var(--ink); }

  /* Front label */
  .label-front {
    position: absolute; left: 80px; top: 48px; width: 644px; height: 230px;
    background: var(--paper);
    border-left: 10px solid var(--ink); border-right: 10px solid var(--ink);
    border-radius: 10px;
  }
  .brand-dot {
    position: absolute; left: 343px; top: 19px; width: 106px; height: 106px;
    margin-left: -80px; border-radius: 50%; background: var(--ink);
  }
  .brand-name {
    position: absolute; left: 0; right: 0; top: 130px; text-align: center;
    font-family: "Josefin Slab", serif; font-weight: 400; font-size: 33px; letter-spacing: 1px;
  }
  .origin {
    position: absolute; left: 0; right: 0; top: 193px; text-align: center;
    font-family: "Josefin Sans", sans-serif; font-weight: 700; font-size: 19px;
  }

  /* Swing tag reverse */
  .tag {
    position: absolute; left: 275px; top: 328px; width: 270px; height: 820px;
    background: var(--paper); border-top: 9px solid var(--ink);
    border-radius: 12px; overflow: visible;
  }
  .tag-hole {
    position: absolute; left: 126px; top: 14px; width: 18px; height: 18px;
    border-radius: 50%; background: var(--backdrop); border: 1.5px solid var(--ink);
  }
  .section-band {
    position: absolute; left: 0; width: 270px; height: 33px; background: var(--ink);
    color: var(--paper); text-align: center; line-height: 35px;
    font-family: "Arvo", serif; font-weight: 700; font-size: 20px;
  }
  .section-band::after {
    content: ""; position: absolute; top: 32px; width: 0; height: 0;
    border-left: 14px solid transparent; border-right: 14px solid transparent;
    border-top: 13px solid var(--ink);
  }
  .band-body { top: 36px; }
  .band-body::after { left: 29px; }
  .band-colours { top: 587px; }
  .band-colours::after { left: 121px; }

  .shape-row { position: absolute; left: 0; width: 270px; height: 64px; }
  .tick-circle {
    position: absolute; left: 24px; top: 12px; width: 40px; height: 40px;
    border: 2px solid var(--ink); border-radius: 50%;
  }
  .figure-sketch {
    position: absolute; left: 88px; top: 2px; width: 30px; height: 60px;
    border-radius: 10px 10px 6px 6px;
    background: linear-gradient(180deg, var(--blush-soft) 0%, var(--blush) 60%, var(--blush-soft) 100%);
  }
  .shape-name {
    position: absolute; left: 141px; top: 50%; transform: translateY(-50%);
    font-family: "Arvo", serif; font-weight: 700; font-size: 15.5px; line-height: 20px;
  }

  .tone { position: absolute; top: 644px; width: 90px; text-align: center; }
  .tone-dot { width: 35px; height: 35px; border-radius: 50%; background: var(--blush); margin: 0 auto; }
  .tone-name { margin-top: 11px; font-family: "Arvo", serif; font-weight: 700; font-size: 14px; }

  .contact-rule { position: absolute; left: 45px; top: 717px; width: 200px; height: 1.5px; background: var(--ink); }
  .contact-phone {
    position: absolute; left: 0; right: 0; top: 728px; text-align: center;
    font-family: "Josefin Sans", sans-serif; font-weight: 700; font-size: 24px;
  }
  .contact-line {
    position: absolute; left: 0; right: 0; text-align: center;
    font-family: "Arvo", serif; font-weight: 700; font-size: 12.5px;
  }
  .contact-email { top: 764px; }
  .contact-web { top: 787px; }
</style>
</head>
<body>

<section class="label-front">
  <div class="brand-dot" style="margin-left:0;left:259px;"></div>
  <div class="brand-name">lantern &amp; moss</div>
  <div class="origin">Made in Australia</div>
</section>

<section class="tag">
  <div class="tag-hole"></div>

  <div class="section-band band-body">BODY TYPE</div>

  <div class="shape-row" style="top:94px;">
    <div class="tick-circle"></div>
    <div class="figure-sketch" role="img" aria-label="Figure sketch with triangle body shape shaded"></div>
    <div class="shape-name">Triangle</div>
  </div>
  <div class="shape-row" style="top:176px;">
    <div class="tick-circle"></div>
    <div class="figure-sketch" role="img" aria-label="Figure sketch with rectangle body shape shaded"></div>
    <div class="shape-name">Recangle</div>
  </div>
  <div class="shape-row" style="top:261px;">
    <div class="tick-circle"></div>
    <div class="figure-sketch" role="img" aria-label="Figure sketch with inverted triangle body shape shaded"></div>
    <div class="shape-name">Inverted<br>Triangle</div>
  </div>
  <div class="shape-row" style="top:341px;">
    <div class="tick-circle"></div>
    <div class="figure-sketch" role="img" aria-label="Figure sketch with hourglass body shape shaded"></div>
    <div class="shape-name">Hourglass</div>
  </div>
  <div class="shape-row" style="top:420px;">
    <div class="tick-circle"></div>
    <div class="figure-sketch" role="img" aria-label="Figure sketch with round body shape shaded"></div>
    <div class="shape-name">Round</div>
  </div>
  <div class="shape-row" style="top:497px;">
    <div class="tick-circle"></div>
    <div class="figure-sketch" role="img" aria-label="Figure sketch with diamond body shape shaded"></div>
    <div class="shape-name">Diamond</div>
  </div>

  <div class="section-band band-colours">COLOURS</div>

  <div class="tone" style="left:-1px;"><div class="tone-dot"></div><div class="tone-name">Warm</div></div>
  <div class="tone" style="left:90px;"><div class="tone-dot"></div><div class="tone-name">Neutral</div></div>
  <div class="tone" style="left:183px;"><div class="tone-dot"></div><div class="tone-name">Cold</div></div>

  <div class="contact-rule"></div>
  <div class="contact-phone">02 948 31 207</div>
  <div class="contact-line contact-email">hello@lanternandmoss.com.au</div>
  <div class="contact-line contact-web">www.lanternandmoss.com.au</div>
</section>

</body>
</html>
```